Electrician Needs A Business Card

I already have a logo and would like a business card to be designed based around this logo the company is called Coralwood Electrical Pty Ltd

The business card will be printed on transparent plastic so I need it to stand out from the crowd. I do not want the card to have anything to do with Electrical on it eg light bulbs, power points etc

I need it to have the following details.

Dominic Farrow
Mobile : 0452 317 908
email : dominic@coralwoodelectrical.com.au

If it could incorporate the following onto the bottom of the card
ELECTRICAL - COMMUNICATIONS - AUDIO - VISUAL

```html
<!DOCTYPE html>
<html lang="en">
<head>
<meta charset="utf-8">
<title>Coralwood Electrical – Business Card</title>
<link href="https://fonts.googleapis.com/css2?family=Noto+Sans:ital,wght@0,400;0,500;1,400&display=swap" rel="stylesheet">
<style>
  :root {
    --backdrop: #e9e6e0;
    --card: #e4dfd6;
    --ink: #161412;
    --accent: #f2a81d;
    --tagline: #a87a22;
    --pattern-grey: #9a9690;
    --pattern-amber: #f1c77b;
  }
  * { margin: 0; padding: 0; box-sizing: border-box; }
  html, body {
    width: 1200px;
    height: 1000px;
    overflow: hidden;
    background: var(--backdrop);
    font-family: "Noto Sans", "Open Sans", sans-serif;
  }
  .card {
    position: absolute;
    left: 152px;
    top: 163px;
    width: 896px;
    height: 554px;
    background: var(--card);
    box-shadow: 0 2px 10px rgba(0, 0, 0, 0.18);
    overflow: hidden;
  }
  .card__decoration {
    position: absolute;
    left: 0;
    top: 142px;
    width: 413px;
    height: 412px;
    background: linear-gradient(180deg, var(--pattern-grey) 0%, var(--pattern-grey) 35%, var(--pattern-amber) 55%, var(--pattern-amber) 100%);
    opacity: 0.55;
  }
  .brand {
    position: absolute;
    left: 448px;
    top: 90px;
    display: flex;
    align-items: center;
    gap: 18px;
  }
  .brand__mark {
    width: 110px;
    height: 110px;
    background: var(--accent);
  }
  .brand__name {
    font-size: 40px;
    font-weight: 400;
    line-height: 1.05;
    color: var(--ink);
  }
  .person {
    position: absolute;
    left: 448px;
    top: 298px;
  }
  .person__name {
    font-size: 25px;
    font-weight: 400;
    color: var(--ink);
    margin-bottom: 22px;
  }
  .contact {
    list-style: none;
    font-size: 17px;
    color: var(--ink);
  }
  .contact__item {
    display: flex;
    align-items: center;
    gap: 12px;
    height: 27px;
  }
  .contact__icon { width: 26px; height: 18px; flex: none; }
  .tagline {
    position: absolute;
    left: 110px;
    top: 486px;
    font-size: 26px;
    font-style: italic;
    letter-spacing: 1px;
    color: var(--tagline);
    white-space: nowrap;
  }
</style>
</head>
<body>
  <article class="card">
    <div class="card__decoration" role="img" aria-label="Large faint geometric brand decoration in grey and amber"></div>

    <header class="brand">
      <div class="brand__mark"></div>
      <div class="brand__name">Coralwood<br>Electrical</div>
    </header>

    <section class="person">
      <h1 class="person__name">Dominic Farrow</h1>
      <ul class="contact">
        <li class="contact__item">
          <svg class="contact__icon" viewBox="0 0 26 18" aria-hidden="true">
            <path d="M2 7 C2 2 24 2 24 7 L24 8 L18 8 L18 5 L8 5 L8 8 L2 8 Z" fill="#f2a81d"/>
            <path d="M7 8 L19 8 L22 16 L4 16 Z" fill="#f2a81d"/>
            <circle cx="13" cy="12" r="2.5" fill="#e4dfd6"/>
          </svg>
          <span>0452 317 908</span>
        </li>
        <li class="contact__item">
          <svg class="contact__icon" viewBox="0 0 26 18" aria-hidden="true">
            <rect x="2" y="2" width="22" height="14" fill="#f2a81d"/>
            <path d="M2 2 L13 10 L24 2" fill="none" stroke="#e4dfd6" stroke-width="1.6"/>
            <path d="M2 16 L10 8 M24 16 L16 8" stroke="#e4dfd6" stroke-width="1.2"/>
          </svg>
          <span>dominic@coralwoodelectrical.com.au</span>
        </li>
      </ul>
    </section>

    <p class="tagline">ELECTRICAL - COMMUNICATIONS - AUDIO - VISUAL</p>
  </article>
</body>
</html>
```